Wix Website Refresh and Redesign

Looking to update and refresh my Wix site. Psychotherapist specializing in treating Anxiety and OCD. Need something warm, professional, and inviting. Nothing super fancy, but needs to look well-designed and professional. I would also like a logo for my business Quiet Harbor. I would like the logo worked into the design.

```html
<!DOCTYPE html>
<html lang="en">
<head>
<meta charset="utf-8">
<title>Quiet Harbor – Anxiety and OCD Therapy</title>
<link href="https://fonts.googleapis.com/css2?family=Saira:wght@500;600&family=Poppins:wght@400;500&display=swap" rel="stylesheet">
<style>
:root{
  --blue:#1b9fdb;
  --ink:#222;
  --body:#333;
  --cream:#f5f3ef;
  --night:#141414;
  --line:#c9c9c9;
}
*{box-sizing:border-box;margin:0;padding:0}
html,body{width:1200px;height:3012px;overflow:hidden;background:#fff}
body{position:relative;font-family:'Poppins',sans-serif;color:var(--body)}
.abs{position:absolute}
.display{font-family:'Saira',sans-serif;font-weight:500;text-transform:uppercase}
.btn{position:absolute;display:flex;align-items:center;justify-content:center;background:var(--blue);color:#fff;border-radius:30px;font-family:'Saira',sans-serif;font-weight:500;text-transform:uppercase;font-size:18px}
/* header */
.topbar{left:0;top:0;width:1200px;height:44px;background:#000}
.header-wedge{left:0;top:0;width:1200px;height:132px}
.brand-mark{left:204px;top:16px;width:34px;height:34px;border-radius:50%;background:var(--blue)}
.brand-name{left:0;width:442px;top:66px;text-align:center;color:var(--blue);font-size:20px}
.brand-sub{left:0;width:442px;top:102px;text-align:center;color:var(--ink);font-size:20px}
.search{left:643px;top:10px;width:236px;height:28px;border:1px solid #fff;border-radius:6px;color:#fff;font-size:8px;padding:9px 18px}
.social{top:11px;width:26px;height:26px;border:1.5px solid #fff;border-radius:50%}
.nav{left:417px;top:84px;display:flex;gap:23px;font-size:18px;color:#111}
.nav .on{color:var(--blue)}
/* hero */
.hero{left:0;top:132px;width:1200px;height:514px;background:linear-gradient(90deg,#efe8e0 0%,#e9dfd3 45%,#8a7564 62%,#6b5b4d 78%,#c9b8a6 100%)}
.hero-heading{left:56px;top:174px;font-size:27px;line-height:43px}
.hero-title{color:var(--blue)}
.hero-loc{color:var(--ink)}
.hero-role{left:58px;top:272px;font-size:21px;line-height:42px;color:var(--ink)}
.hero-copy{left:58px;top:364px;width:550px;font-size:15.5px;line-height:31px;color:#333}
/* intro */
.ornament{height:30px}
.ornament i{position:absolute;top:14px;width:62px;height:1px;background:#8aa}
.ornament b{position:absolute;left:72px;top:0;width:30px;height:30px;border-radius:50%;background:var(--blue)}
.section-title{color:var(--blue);font-size:32px;text-align:center;width:1200px;left:0}
.intro{left:200px;top:848px;width:800px;text-align:center;font-size:15.5px;line-height:31px}
.col{top:1022px;width:300px}
.col .icon{position:absolute;left:0;top:4px;width:50px;height:50px}
.col h3{position:absolute;left:74px;top:0;font-family:'Saira',sans-serif;font-weight:500;text-transform:uppercase;color:var(--blue);font-size:20px;line-height:33px;width:240px}
.col p{position:absolute;left:0;top:87px;width:290px;font-size:15.5px;line-height:30px}
.divider{top:1018px;width:1px;height:342px;background:var(--line)}
/* about */
.about{left:0;top:1443px;width:1200px;height:444px;background:var(--cream)}
.about-photo{left:111px;top:1476px;width:420px;height:378px;border-radius:4px;background:linear-gradient(160deg,#b8a68d,#8a7a64 50%,#3d5f94 80%)}
.about-title{left:578px;top:1518px;color:var(--blue);font-size:37px}
.about-copy{left:578px;top:1584px;width:520px;font-size:15.5px;line-height:31px}
/* video */
.video{left:111px;top:1973px;width:978px;height:468px;border-radius:6px;background:linear-gradient(90deg,#d6c8a6 0%,#f1e6b8 20%,#a89880 45%,#b59c86 65%,#4b4f56 100%)}
.play{left:568px;top:2175px;width:64px;height:64px;border-radius:50%;background:var(--blue);border:4px solid rgba(255,255,255,.6)}
/* footer */
.footer{left:0;top:2535px;width:1200px;height:477px;background:var(--night);color:#fff}
.foot-mark{left:118px;top:2590px;width:42px;height:42px;border-radius:50%;background:var(--blue)}
.foot-name{left:117px;top:2654px;color:var(--blue);font-size:22px}
.foot-sub{left:117px;top:2688px;font-size:22px;color:#fff}
.foot-copy{left:115px;top:2735px;width:380px;font-size:16px;line-height:31px;color:#fff}
.contact-box{left:539px;top:2592px;width:333px;height:310px;border:1px solid #bbb;border-radius:3px}
.contact-title{left:539px;top:2628px;width:333px;text-align:center;color:var(--blue);font-size:21px}
.c-row{left:630px;font-size:16px;line-height:36px;color:#fff}
.c-ico{left:578px}
.links-title{left:938px;top:2618px;color:var(--blue);font-size:22px}
.links{left:938px;top:2660px;font-size:16px;line-height:31.5px;color:#fff;list-style:none}
.foot-rule{left:111px;top:2958px;width:978px;height:1px;background:#444}
.copyright{left:0;width:1200px;top:2975px;text-align:center;font-size:15px;color:#fff}
</style>
</head>
<body>

<header>
  <div class="abs topbar"></div>
  <svg class="abs header-wedge" viewBox="0 0 1200 132" aria-hidden="true">
    <polygon points="0,0 442,0 470,44 1200,44 1200,132 0,132" fill="#fff"/>
  </svg>
  <div class="abs brand-mark"></div>
  <div class="abs display brand-name">Quiet Harbor</div>
  <div class="abs display brand-sub">Daniel Reyes, LCSW</div>
  <div class="abs search display">Search</div>
  <svg class="abs" style="left:851px;top:16px" width="16" height="16" viewBox="0 0 16 16" aria-hidden="true"><circle cx="6.5" cy="6.5" r="5" fill="none" stroke="#fff" stroke-width="1.6"/><line x1="10.5" y1="10.5" x2="15" y2="15" stroke="#fff" stroke-width="1.6"/></svg>
  <div class="abs social" style="left:968px"></div>
  <div class="abs social" style="left:998px"></div>
  <div class="abs social" style="left:1028px"></div>
  <div class="abs social" style="left:1058px"></div>
  <nav class="abs nav display">
    <span class="on">Home</span><span>Therapy</span><span>OCD</span><span>Anxiety Disorders</span><span>About Daniel</span><span>Contact</span><span>Blog</span>
  </nav>
</header>

<section>
  <div class="abs hero" role="img" aria-label="Photo of a man resting his head in his hand in a softly lit room"></div>
  <h1 class="abs display hero-heading"><span class="hero-title">Evidence-based anxiety and OCD treatment -</span><br><span class="hero-loc">Denver, Colorado</span></h1>
  <div class="abs display hero-role">Daniel Reyes, LCSW<br>Online and in-person anxiety therapist (Denver, CO)</div>
  <p class="abs hero-copy">Maybe you're here because you're wrestling with the challenges of OCD or Anxiety. Or maybe, you're here because you're worried about a friend or a loved one. Whatever the reason, I'm glad you're here. And here's what's most important to know: with the right evidence-based therapy, freedom from OCD</p>
  <div class="btn" style="left:59px;top:542px;width:397px;height:58px">Schedule a free online consultation</div>
</section>

<section>
  <div class="abs ornament" style="left:546px;top:736px;width:180px"><i style="left:0"></i><b></b><i style="left:114px"></i></div>
  <h2 class="abs display section-title" style="top:788px">Anxiety therapy Denver, Colorado</h2>
  <p class="abs intro">I differ from a general therapist in that I specialize in only a few select disorders and treatments. I have spent the last decade exclusively studying and treating OCD and Anxiety. What does this mean for you? You get expert, evidence-based therapy from a therapist experienced in all aspects of these disorders.</p>

  <div class="abs col" style="left:110px">
    <svg class="icon" viewBox="0 0 50 50" aria-hidden="true"><circle cx="25" cy="23" r="19" fill="none" stroke="#1b9fdb" stroke-width="2"/><path d="M16 44v-6M34 44v-6" stroke="#1b9fdb" stroke-width="2"/></svg>
    <h3>Obsessive Compulsive Disorder (OCD)</h3>
    <p>Navigating life with Obsessive-Compulsive Disorder might seem daunting, yet there is a silver lining: it is highly treatable, particularly with the help of an experienced OCD specialist.</p>
  </div>
  <div class="abs divider" style="left:434px"></div>
  <div class="abs col" style="left:465px">
    <svg class="icon" viewBox="0 0 50 50" aria-hidden="true"><circle cx="25" cy="16" r="12" fill="none" stroke="#1b9fdb" stroke-width="2"/><path d="M4 22l4 20h8M46 22l-4 20h-8" fill="none" stroke="#1b9fdb" stroke-width="2"/></svg>
    <h3>Anxiety disorder therapy</h3>
    <p>Anxiety Disorders rank as the most prevalent mental health condition in the United States, impacting around 40 million adults. The reach of these disorders extends further, affecting a teenagers and children</p>
  </div>
  <div class="abs divider" style="left:780px"></div>
  <div class="abs col" style="left:815px">
    <svg class="icon" viewBox="0 0 50 50" aria-hidden="true"><circle cx="26" cy="22" r="19" fill="none" stroke="#1b9fdb" stroke-width="2"/><path d="M26 14v14M19 21h14" stroke="#1b9fdb" stroke-width="2.5"/></svg>
    <h3>Evidence-based therapy</h3>
    <p>Exposure Therapy is an essential component in the treatment of anxiety disorders. Put simply, our brains don't change much unless our behaviors change as well. We can talk about the anxious mind's</p>
  </div>
  <div class="btn" style="left:111px;top:1307px;width:125px;height:50px">Read more</div>
  <div class="btn" style="left:465px;top:1307px;width:125px;height:50px">Read more</div>
  <div class="btn" style="left:816px;top:1307px;width:125px;height:50px">Read more</div>
</section>

<section>
  <div class="abs about"></div>
  <div class="abs about-photo" role="img" aria-label="Portrait of Daniel Reyes in a blue blazer outdoors"></div>
  <div class="abs ornament" style="left:578px;top:1467px;width:180px"><i style="left:0"></i><b></b><i style="left:114px"></i></div>
  <h2 class="abs display about-title">Daniel Reyes, LCSW</h2>
  <p class="abs about-copy">Hi, I'm Daniel Reyes, a Licensed Psychotherapist and Clinical Social Worker in Denver, Colorado. I specialize in the treatment of Obsessive-Compulsive Disorder (OCD) and Anxiety Disorders including Generalized Anxiety Disorder, Social Anxiety Disorder, Panic Disorder, Health Anxiety, and Phobias. I have spent the last 10+ years guiding and</p>
  <div class="btn" style="left:578px;top:1796px;width:165px;height:58px">Learn more</div>
</section>

<section>
  <div class="abs video" role="img" aria-label="Video still of Daniel Reyes speaking in his office beside a lamp"></div>
  <div class="abs play"></div>
  <svg class="abs" style="left:594px;top:2198px" width="18" height="20" viewBox="0 0 18 20" aria-hidden="true"><polygon points="2,1 17,10 2,19" fill="#fff"/></svg>
</section>

<footer>
  <div class="abs footer"></div>
  <div class="abs foot-mark"></div>
  <div class="abs display foot-name">Quiet Harbor</div>
  <div class="abs display foot-sub">Daniel Reyes, LCSW</div>
  <p class="abs foot-copy">Living with OCD or Anxiety can feel like navigating an endless maze with no real exit. You're trapped in a cycle of persistent worry and intrusive thoughts, like being caught in a relentless storm of 'what ifs.</p>

  <div class="abs contact-box"></div>
  <div class="abs display contact-title">Contact us</div>
  <svg class="abs c-ico" style="top:2697px" width="22" height="26" viewBox="0 0 22 26" aria-hidden="true"><path d="M11 25C4 16 2 12 2 9a9 9 0 0 1 18 0c0 3-2 7-9 16z" fill="#1b9fdb"/><circle cx="11" cy="9" r="3.5" fill="#141414"/></svg>
  <div class="abs c-row" style="top:2690px">418 Alder Ridge Lane<br>Alder Springs, CO 80999</div>
  <svg class="abs c-ico" style="top:2780px" width="20" height="20" viewBox="0 0 24 24" aria-hidden="true"><path d="M6.6 10.8a15 15 0 0 0 6.6 6.6l2.2-2.2a1 1 0 0 1 1-.25 11 11 0 0 0 3.6.6 1 1 0 0 1 1 1V20a1 1 0 0 1-1 1A17 17 0 0 1 3 4a1 1 0 0 1 1-1h3.5a1 1 0 0 1 1 1c0 1.25.2 2.45.6 3.6a1 1 0 0 1-.25 1z" fill="#1b9fdb"/></svg>
  <div class="abs c-row" style="top:2772px">303-555-0142</div>
  <svg class="abs c-ico" style="top:2828px" width="20" height="14" viewBox="0 0 20 14" aria-hidden="true"><rect width="20" height="14" rx="1" fill="#1b9fdb"/><path d="M1 1l9 7 9-7" fill="none" stroke="#141414" stroke-width="1.5"/></svg>
  <div class="abs c-row" style="top:2817px">hello@quietharbor.com</div>

  <div class="abs display links-title">Quick links</div>
  <ul class="abs links">
    <li>Home</li><li>Therapy</li><li>OCD</li><li>Anxiety Disorders</li><li>About Daniel</li><li>Contact</li><li>Blog</li>
  </ul>

  <div class="abs foot-rule"></div>
  <div class="abs display copyright">@2024 Copyrights. All rights reserved.</div>
</footer>

</body>
</html>
```